依頼詳細
表面はカラー、裏面は白黒で申し込み用紙にしようと考えています。
魅力のあるツアーだと思いますので、読み手に伝わるよう作成をお願いします。
〈ツアーのポイント〉
・透き通った青い海、緑の山々、満天の星空など、大自然に囲まれたダイナミックな眺望
・貸切バスで観光スポットをご案内
・地元の食材にこだわった料理を堪能
・島人との交流
・自然の中でBBQ、キャンプファイヤー
・宿泊は神津島唯一の温泉宿
・カップル成立で特典付き
・格安
など
多少変更が出るかもしれませんので、こちらでも編集できる形式で納品をお願いします。
ご不明点などありましたらご連絡ください。
よろしくお願いいたします。
記載項目
表現など変更して頂いて結構です。

【表面】
独身女性参加者募集
〈イベント名称〉渚トーク星結び
〈日時〉2015年7月3日(金)~2015年7月5日(日)
〈会場〉神津島
〈ツアースケジュール〉
1日目 20:00 東京 灯波客船ターミナル集合(女性のみ)・女子会
23:00 出航(大型客船)
2日目 9:00 神津島着・チェックイン
朝 男性合流・アイスブレイク
昼 昼食・島内観光
夜 BBQ・キャンプファイヤー・温泉旅館宿泊
3日目 朝 自由時間
13:35 神津島発
17:30 東京 灯波客船ターミナル着・解散
〈ツアーのポイント〉依頼詳細参考
〈集合場所〉白浪航路灯波港 1階ロビー ※若葉環状線蓮見坂駅から徒歩8分
〈集合時間〉2015年7月3日(金)20:00
〈参加対象〉20歳~35歳の島外在住独身女性
〈募集人数〉15名(先着順)
〈参加料金〉15,000円/1人(交通費・宿泊費・食費込み)
〈申込方法〉裏面の申込書にご記入の上、メール・FAX・郵送にてお申込みください。
〈申込締切〉2015年6月7日(日)
〈ホームページ〉
※ホームページのURLを載せたいのですが、まだ出来上がっていないので後ほどURLを追加できるようにしていただきたいです。

裏面は補足情報に記載します。
サイズ
A4
ページ数
両面
希望イメージ
• +5 0 +5
• シンプル
複雑
• 単色
カラフル
• 暗い
明るい
• 日常
高級
• 遊び心
厳粛
• 未来的
伝統的
• 女性的
男性的
希望する色
赤系、水色系、緑系、黄・オレンジ系
納品ファイル
補足説明
【裏面】申込用紙
〈イベント名称〉
〈日時〉
〈会場〉
〈募集人数〉15名(先着順)
〈参加資格〉20歳から35歳までの神津島外在住の独身女性
お一人様参加・シングルマザー・結婚歴あり歓迎
〈参加料金〉
MAIL  shiomi@hx.nagisanet-example.jp
メールでのお申し込みは①氏名②生年月日③住所④電話番号⑤メールアドレスを添えて上記のアドレスまでご送信ください。
FAX 04992-7-5530
〈申し込みフォーム〉
・氏名(ふりがな)
・氏名
・生年月日
・電話番号
・メールアドレス
・自己PR
〈注意事項〉
1 申し込み・キャンセルは6月7日(日)までにお願いします。
2 男女比は出来る限り調整しますが同数にならないこともありますのでご了承願います。
3 個人情報は厳重に管理し、本事業のみの使用とさせていただきます。
4 悪天候時はプログラム内容を変更または中止する場合があります。

申し込み受付後、事務局より順次詳細をお送りいたします。

問い合わせ・お申込み 汐見村商工会青年部事務局
〒100-0999 東京都汐見村汐見村2483番地
TEL  04992-7-4418
FAX  04992-7-5530

依頼公開後の追記内容
写真を添付します。

ターゲット層を対象にアンケート調査を実施した結果、最も多く票が集まったため。

この度は私どもの為に、多数ご提案をご用意していただき、誠にありがとうございます。どの提案も魅力を感じていましたが、上記の理由から一社選ばせていただきました。
折角親身にお世話をしていただいたところ、心苦しい限りですが、ご理解いただければ幸いです。
また、同様の機会があればよろしくお願いいたします。

```html
<!DOCTYPE html>
<html lang="ja">
<head>
<meta charset="utf-8">
<title>渚トーク星結び in 神津島</title>
<link rel="stylesheet" href="https://fonts.googleapis.com/css2?family=M+PLUS+Rounded+1c:wght@500;800;900&family=Noto+Sans+JP:wght@400;700;900&display=swap">
<style>
:root{
  --sea-deep:#1f6fa8;
  --sea:#4aa8d8;
  --title:#1b7fc4;
  --orange:#f08a1c;
  --red:#e23b2e;
  --yellow:#ffe23a;
  --green:#4e9a3c;
  --ink:#2a2a2a;
  --pink:#f6c9d3;
  --paper:#ffffff;
}
*{margin:0;padding:0;box-sizing:border-box}
html,body{width:846px;height:1200px;overflow:hidden;background:var(--paper)}
body{font-family:"Noto Sans JP",sans-serif;color:var(--ink)}
.flyer{position:relative;width:846px;height:1200px;overflow:hidden;
  background:linear-gradient(180deg,#fff 0,#fff 55%,#eaf6fc 100%)}
.hero-photo{position:absolute;left:0;top:0;width:846px;height:560px;
  background:linear-gradient(180deg,#5fb4e3 0%,#8ccbe9 22%,#2a8cc0 38%,#3bb0c9 55%,#bfe6f3 78%,rgba(255,255,255,0) 100%)}
.vertical-word{position:absolute;left:22px;top:30px;writing-mode:vertical-rl;
  font-family:"M PLUS Rounded 1c",sans-serif;font-weight:800;font-size:72px;letter-spacing:8px;
  color:rgba(255,255,255,.45)}
.photo-circle{position:absolute;border-radius:50%;border:5px solid #fff;box-shadow:0 2px 6px rgba(0,0,0,.25)}
.c-sea{left:650px;top:-20px;width:200px;height:200px;background:radial-gradient(circle,#6fc3e8,#1f6fa8)}
.c-sunset{left:680px;top:150px;width:160px;height:160px;background:radial-gradient(circle,#ffb347,#a53b1a 70%,#2b1a2e)}
.c-beach{left:560px;top:170px;width:110px;height:110px;background:radial-gradient(circle,#f4e3b5,#53a9cf)}
.hero-copy{position:absolute;left:430px;top:20px;width:220px;font-weight:700;font-size:17px;line-height:1.6;color:#fff;
  text-shadow:0 0 4px rgba(0,50,90,.8);transform:rotate(-14deg)}
.hero-tag{position:absolute;left:360px;top:150px;font-family:"M PLUS Rounded 1c",sans-serif;font-weight:900;font-size:22px;
  color:var(--yellow);text-shadow:0 0 4px #0b4b7a,0 0 2px #0b4b7a;transform:rotate(-20deg)}
.recruit{position:absolute;left:330px;top:432px;font-family:"M PLUS Rounded 1c",sans-serif;font-weight:900;font-size:38px;
  color:var(--orange);text-shadow:0 0 3px #fff,0 0 6px #fff}
.event-title{position:absolute;left:20px;top:488px;width:806px;text-align:center;white-space:nowrap;
  font-family:"M PLUS Rounded 1c",sans-serif;font-weight:900;font-size:70px;line-height:1;color:var(--title);
  text-shadow:3px 3px 0 #fff,-3px -3px 0 #fff,3px -3px 0 #fff,-3px 3px 0 #fff,0 6px 10px rgba(0,60,110,.3)}
.event-title small{font-size:50px}
.dates{position:absolute;left:20px;top:568px;width:806px;text-align:center;font-weight:900;font-size:32px;color:var(--sea-deep)}
.info{position:absolute;left:34px;top:618px;width:540px;font-size:14px;line-height:1.45}
.info dt{float:left;width:105px;font-weight:700;color:var(--sea-deep)}
.info dd{margin-left:105px}
.cliff-photo{position:absolute;left:590px;top:620px;width:240px;height:160px;border:4px solid #fff;
  background:linear-gradient(160deg,#8cc8e6,#e8e5d9 55%,#b9b3a2);box-shadow:0 2px 6px rgba(0,0,0,.2)}
.cheap{position:absolute;left:640px;top:770px;font-family:"M PLUS Rounded 1c",sans-serif;font-weight:900;font-size:40px;color:var(--red);
  text-shadow:0 0 3px #fff;transform:rotate(-6deg)}
.schedule-label{position:absolute;left:26px;top:822px;padding:2px 14px;background:var(--pink);border-radius:20px;
  font-weight:900;font-size:22px;color:var(--red)}
.schedule{position:absolute;left:230px;top:860px;width:525px;background:rgba(255,255,255,.92);
  border:3px solid var(--sea);border-radius:14px;padding:8px 18px;font-size:14.5px;line-height:1.45}
.day{display:grid;grid-template-columns:60px 56px 1fr;padding:3px 0;border-bottom:1px dashed var(--sea)}
.day:last-child{border-bottom:none}
.day .label{font-weight:900;color:var(--sea-deep);font-size:17px}
.day .time{font-weight:700}
.day .end{grid-column:3;color:#555}
.side-circle{position:absolute;border-radius:50%;border:4px solid #fff;box-shadow:0 2px 6px rgba(0,0,0,.25)}
.s-ship{left:20px;top:870px;width:180px;height:120px;border-radius:14px;background:linear-gradient(180deg,#9bd2ef,#2c6ea3)}
.s-food{left:20px;top:1000px;width:190px;height:135px;background:radial-gradient(circle,#f7a68f,#c0392b)}
.s-onsen{left:770px;top:860px;width:70px;height:70px;background:radial-gradient(circle,#e9d7b3,#8e6b48)}
.s-bus{left:770px;top:1060px;width:70px;height:75px;border-radius:12px;background:linear-gradient(180deg,#f0b35a,#3a2a44)}
.side-text{position:absolute;font-weight:900;font-family:"M PLUS Rounded 1c",sans-serif}
.t-ship{left:40px;top:880px;font-size:26px;color:var(--red);text-shadow:0 0 3px #fff}
.t-food{left:25px;top:1048px;width:180px;font-size:15px;color:#fff;text-align:center;text-shadow:0 0 3px #7a1b12}
.t-onsen{left:763px;top:936px;width:80px;font-size:13px;line-height:1.3;color:var(--red);background:#fff;padding:2px 4px;border-radius:8px}
.t-bus{left:763px;top:980px;width:80px;font-size:13px;line-height:1.3;color:var(--green);background:#fff;padding:2px 4px;border-radius:8px}
.couple{position:absolute;left:0;top:1148px;width:846px;text-align:center;font-family:"M PLUS Rounded 1c",sans-serif;
  font-weight:900;font-size:28px;color:var(--red)}
</style>
</head>
<body>
<main class="flyer">
  <div class="hero-photo" role="img" aria-label="透き通った青い海と緑の山々の島の海岸風景"></div>
  <div class="vertical-word">KOUZUSHIMA</div>
  <div class="photo-circle c-sea" role="img" aria-label="青い海の写真"></div>
  <div class="photo-circle c-sunset" role="img" aria-label="夕焼けの海の写真"></div>
  <div class="photo-circle c-beach" role="img" aria-label="白い砂浜の写真"></div>
  <p class="hero-copy">透き通った青い海、緑の山々、満天の星空など…</p>
  <p class="hero-tag">大自然に囲まれたダイナミックな眺望!</p>

  <p class="recruit">独身女性参加者募集!</p>
  <h1 class="event-title">渚トーク星結び<small>in</small>神津島</h1>
  <p class="dates">2015年7月3日(金)〜2015年7月5日(日)</p>

  <dl class="info">
    <dt>〈集合場所〉</dt><dd>白浪航路灯波港 1階ロビー ※若葉環状線蓮見坂駅から徒歩8分</dd>
    <dt>〈集合時間〉</dt><dd>2015年7月3日(金)20:00</dd>
    <dt>〈参加対象〉</dt><dd>20歳〜35歳の島外在住独身女性</dd>
    <dt>〈募集人数〉</dt><dd>15名(先着順)</dd>
    <dt>〈参加料金〉</dt><dd>15,000円/1人(交通費・宿泊費・食費込み)</dd>
    <dt>〈申込方法〉</dt><dd>裏面の申込書にご記入の上、メール・FAX・郵送にてお申込みください。</dd>
    <dt>〈申込締切〉</dt><dd>2015年6月7日(日)</dd>
    <dt>〈ホームページ〉</dt><dd>&nbsp;</dd>
  </dl>

  <div class="cliff-photo" role="img" aria-label="白い断崖と海の写真"></div>
  <p class="cheap">格安!</p>

  <h2 class="schedule-label">★ツアースケジュール★</h2>
  <section class="schedule">
    <div class="day">
      <span class="label">1日目</span><span class="time">20:00</span><span>東京 灯波客船ターミナル集合(女性のみ)・女子会</span>
      <span></span><span class="time">23:00</span><span>出航(大型客船)</span>
      <span class="end">1日目終了</span>
    </div>
    <div class="day">
      <span class="label">2日目</span><span class="time">9:00</span><span>神津島着・チェックイン</span>
      <span></span><span class="time">朝</span><span>男性合流・アイスブレイク</span>
      <span></span><span class="time">昼</span><span>昼食・島内観光</span>
      <span></span><span class="time">夜</span><span>BBQ・キャンプファイヤー・温泉旅館宿泊</span>
      <span class="end">2日目終了</span>
    </div>
    <div class="day">
      <span class="label">3日目</span><span class="time">朝</span><span>自由時間</span>
      <span></span><span class="time">13:35</span><span>神津島発</span>
      <span></span><span class="time">17:30</span><span>東京 灯波客船ターミナル着・解散</span>
    </div>
  </section>

  <div class="side-circle s-ship" role="img" aria-label="大型客船の写真"></div>
  <p class="side-text t-ship">出航!</p>
  <div class="side-circle s-food" role="img" aria-label="地元食材の料理の写真"></div>
  <p class="side-text t-food">地元の食材にこだわった料理!</p>
  <div class="side-circle s-onsen" role="img" aria-label="温泉宿の写真"></div>
  <p class="side-text t-onsen">神津島唯一の温泉宿</p>
  <p class="side-text t-bus">貸切バスで観光スポットをご案内!</p>
  <div class="side-circle s-bus" role="img" aria-label="観光スポットの写真"></div>

  <p class="couple">カップル成立で特典付き!</p>
</main>
</body>
</html>
```